Business Card for Interior Designer

I have a logo but want to modify it a little for the business card. Somehow I did it on one of the apps in Adobe - but I'm not proficient enough in adobe to modify it. I'd like to take out the wooden background and make it work for a standard size business card (rectangular not square). I'd also like to have options for the design - Patterns like houndstooth, grass cloth, floral, polkadot - stuff like that but in subtle/classic colors. I also like wreaths (boxwood/magnolia/eucalyptus) and would like to incorporate that as well.

```html
<!DOCTYPE html>
<html lang="en">
<head>
<meta charset="utf-8">
<title>Willow &amp; Fern Interiors – Business Card</title>
<link href="https://fonts.googleapis.com/css2?family=Amatic+SC:wght@700&family=Yeseva+One&display=swap" rel="stylesheet">
<style>
  :root {
    --backdrop: #e8e2d8;
    --card: #ffffff;
    --teal: #3d7e9b;
    --teal-dark: #2f6a85;
    --ink: #2f5f78;
    --wreath-tint: #e4eef3;
  }
  * { margin: 0; padding: 0; box-sizing: border-box; }
  html, body { width: 900px; height: 1200px; overflow: hidden; }
  body { background: var(--backdrop); position: relative; font-family: "Amatic SC", sans-serif; }

  .card {
    position: absolute;
    left: 36px;
    width: 828px;
    height: 432px;
    background: var(--card);
    border-radius: 22px;
    overflow: hidden;
    box-shadow: 0 6px 18px rgba(0,0,0,.18);
  }
  .card--front { top: 110px; }
  .card--back { top: 640px; }

  .pattern-band {
    position: absolute;
    left: 0; right: 0; top: 24px; bottom: 24px;
    background: linear-gradient(180deg, var(--teal) 0%, var(--teal-dark) 100%);
  }
  .logo-disc {
    position: absolute;
    width: 420px; height: 420px;
    left: 204px; top: 6px;
    border-radius: 50%;
    background: var(--card);
    display: flex; align-items: center; justify-content: center;
  }
  .logo-disc--back { left: 24px; width: 380px; height: 380px; top: 26px; }

  .wreath-area {
    width: 330px; height: 330px;
    border-radius: 50%;
    background: var(--wreath-tint);
    display: flex; flex-direction: column; align-items: center; justify-content: center;
    gap: 12px;
  }
  .logo-disc--back .wreath-area { width: 310px; height: 310px; }

  .brand-name {
    font-family: "Yeseva One", serif;
    color: var(--teal);
    font-size: 30px;
    line-height: 1;
    white-space: nowrap;
  }
  .logo-disc--back .brand-name { font-size: 28px; }
  .brand-tagline {
    font-family: "Amatic SC", sans-serif;
    color: var(--ink);
    font-size: 28px;
    line-height: 1;
    letter-spacing: 1px;
  }

  .contact {
    position: absolute;
    left: 440px; top: 96px;
    width: 360px;
    text-align: center;
    color: var(--teal);
  }
  .contact__name {
    font-family: "Yeseva One", serif;
    font-size: 40px;
    font-weight: 400;
    line-height: 1.1;
    white-space: nowrap;
  }
  .contact__role {
    font-size: 26px;
    letter-spacing: 2px;
    margin-top: 6px;
  }
  .contact__dots { display: flex; justify-content: center; gap: 10px; margin: 10px 0 26px; }
  .contact__dots span { width: 10px; height: 10px; border-radius: 50%; background: var(--teal); }
  .contact__line {
    font-size: 30px;
    line-height: 1.1;
    letter-spacing: 1px;
  }
</style>
</head>
<body>

  <section class="card card--front" aria-label="Business card front">
    <div class="pattern-band" role="img" aria-label="Teal and white chevron zigzag pattern"></div>
    <div class="logo-disc">
      <div class="wreath-area" role="img" aria-label="Leafy branch wreath framing the studio name">
        <div class="brand-name">Willow &amp; Fern Interiors</div>
        <div class="brand-tagline">rooms made for living</div>
      </div>
    </div>
  </section>

  <section class="card card--back" aria-label="Business card back">
    <div class="logo-disc logo-disc--back">
      <div class="wreath-area" role="img" aria-label="Leafy branch wreath framing the studio name">
        <div class="brand-name">Willow &amp; Fern Interiors</div>
        <div class="brand-tagline">rooms made for living</div>
      </div>
    </div>

    <div class="contact">
      <h1 class="contact__name">Johnathan Doe</h1>
      <p class="contact__role">OWNER</p>
      <div class="contact__dots"><span></span><span></span><span></span></div>
      <p class="contact__line">123 456 7890</p>
      <p class="contact__line">EMAIL@DOMAIN.COM</p>
      <p class="contact__line">WWW.WEBSITE.COM</p>
    </div>
  </section>

</body>
</html>
```